New business logo / Business Card Design

My company provides Interim Management and consultancy, for Facilities Services. Covers any aspect of facilities management, including M&E, helpdesk, asset management, supplier relationships, catering, cleaning etc. Company provides innovative solutions to exceed client needs, drawing on years of experience. Initial thoughts on logo are attached below. Fits with RAG status on projects, red, amber and green, with logo design colours around moving services from amber to green.

Target Market(s)

Facilities Management clients and service providers

Industry/Entity Type

Business

Contact Information for Business Card

Company Name = k7Rventures Ltd My name on card = Derek Whitcombe, Director Mobile = 07516309842 Email = Derek@k7rventuresltd.co.uk Twitter = @k7Rventures Ltd

Font styles to use
Sans Serif

Colors
f37122
00a990

Requirements
Must have
• Logo to be evident, with some background image in reference to Facilities Management

```html
<!DOCTYPE html>
<html lang="en">
<head>
<meta charset="utf-8">
<title>k7Rventures Ltd – Business Card</title>
<link rel="stylesheet" href="https://fonts.googleapis.com/css2?family=Open+Sans:wght@400;600;800&display=swap">
<style>
  :root {
    --page-bg: #ece7df;
    --card-white: #fbfbfa;
    --card-black: #050505;
    --ink: #2a2a2a;
    --ink-light: #c9c9c9;
    --brand-orange: #e8661f;
    --brand-green: #1f8a3a;
  }
  * { margin: 0; padding: 0; box-sizing: border-box; }
  html, body {
    width: 1200px; height: 800px; overflow: hidden;
    background: var(--page-bg);
    font-family: "Open Sans", Arial, sans-serif;
  }
  .stage {
    position: relative; width: 1200px; height: 800px;
    display: flex; align-items: center; justify-content: center; gap: 40px;
  }
  .card {
    position: relative; width: 520px; height: 306px;
    border-radius: 4px;
    box-shadow: 0 10px 28px rgba(0,0,0,0.18);
    overflow: hidden;
  }
  .card--front { background: var(--card-white); padding: 34px 38px; }
  .card--back {
    background: var(--card-black);
    display: flex; flex-direction: column; align-items: center; justify-content: center;
  }
  .wordmark {
    font-weight: 800; font-size: 40px; letter-spacing: -0.5px; line-height: 1;
    color: var(--ink);
  }
  .card--back .wordmark { color: #f2f2f2; font-size: 36px; }
  .holder {
    margin-top: 20px; font-size: 19px; font-weight: 400; text-transform: uppercase;
    color: var(--brand-orange); letter-spacing: 0.3px;
  }
  .holder .divider { color: var(--brand-orange); font-weight: 600; margin: 0 6px; }
  .holder .role { color: var(--brand-green); font-size: 16px; }
  .contact-list { list-style: none; margin-top: 14px; }
  .contact-list li {
    display: flex; align-items: center; gap: 10px;
    font-size: 15px; color: var(--ink); line-height: 24px;
  }
  .contact-list svg { width: 14px; height: 14px; flex: none; }
  .website-line {
    margin-top: 26px; font-size: 13px; letter-spacing: 1.6px;
    color: var(--ink-light); font-style: normal;
  }
</style>
</head>
<body>
<main class="stage">
  <section class="card card--front" aria-label="Business card front">
    <div class="wordmark">k7Rventures Ltd</div>
    <p class="holder">Derek Whitcombe<span class="divider">|</span><span class="role">Director</span></p>
    <ul class="contact-list">
      <li>
        <svg viewBox="0 0 14 14" aria-hidden="true"><rect x="3" y="0.8" width="8" height="12.4" rx="1.4" fill="none" stroke="var(--brand-orange)" stroke-width="1.6"/><circle cx="7" cy="11" r="0.9" fill="var(--brand-orange)"/></svg>
        07516309842
      </li>
      <li>
        <svg viewBox="0 0 14 14" aria-hidden="true"><circle cx="7" cy="7" r="5.5" fill="var(--brand-orange)"/></svg>
        @k7Rventures Ltd
      </li>
      <li>
        <svg viewBox="0 0 14 14" aria-hidden="true"><rect x="0.5" y="2.5" width="13" height="9" fill="var(--brand-orange)"/><path d="M0.8 3 L7 8 L13.2 3" fill="none" stroke="#fff" stroke-width="1.2"/></svg>
        Derek@k7rventuresltd.co.uk
      </li>
      <li>
        <svg viewBox="0 0 14 14" aria-hidden="true"><circle cx="7" cy="7" r="6" fill="var(--brand-orange)"/><path d="M1 7 H13 M7 1 C4 4 4 10 7 13 M7 1 C10 4 10 10 7 13" fill="none" stroke="#fff" stroke-width="0.9"/></svg>
        www.k7rventuresltd.co.uk
      </li>
    </ul>
  </section>

  <section class="card card--back" aria-label="Business card back">
    <div class="wordmark">k7Rventures Ltd</div>
    <p class="website-line">www.k7rventuresltd.co.uk</p>
  </section>
</main>
</body>
</html>
```